Business Card for a Life Coaching Company

BRAVOAK is a Life Coaching company that was initiated to support people who want to transform thier life or ana aspect of it.
our slogan is : "Dream. Believe. Succeed"
our logo is uploaded.
The name of the company implies that leadership, strength and wisdom required to change your life.
We want an attractive business card that would give an impression of reliability, support and change. so we really want it unique. Here are some examples of unique cards:

http://www.pixelcratehub.com/2009/05/100-really-creative-business-cards/

BravOak is a life coaching organization focusing on individual transformation through the application of relevant and timeless principles of success.  BravOak believes that real, sustainable life transformations are brought about by tuning into the timeless wisdom we each carry in our hearts while boldy acting in the direction of our dreams.

Contacts on the card:
Address: 7 Sharia Nour El Din Zamalek Cairo Egypt
Tel: +202 24 31 57 18
Fax: +202 24 31 57 02
Mobile: +2 012 748 2396 (Dalia Haddad)
+2 0199915815 (Tariq Mansoor)

By the way, our temporary website is http://www.bravoak.com

We have attached an .eps file with various configurations of our logo.

```html
<!DOCTYPE html>
<html lang="en">
<head>
<meta charset="utf-8">
<title>BRAVOAK Business Card</title>
<link rel="stylesheet" href="https://fonts.googleapis.com/css2?family=Montserrat:wght@500&display=swap">
<style>
  :root {
    --card-bg: #ffffff;
    --brand-orange: #ff6a00;
    --brand-orange-soft: #ffb27a;
    --wave-grey: #8a8a8a;
    --name-grey: #8f8f8f;
  }
  html, body {
    margin: 0;
    padding: 0;
    overflow: hidden;
    background: var(--card-bg);
  }
  .card {
    position: relative;
    width: 1200px;
    height: 686px;
    background: var(--card-bg);
    overflow: hidden;
  }
  .card__waves {
    position: absolute;
    inset: 0;
    width: 1200px;
    height: 686px;
  }
  .wave--grey { fill: var(--wave-grey); }
  .wave--orange { fill: var(--brand-orange); }
  .emblem-area {
    position: absolute;
    left: 920px;
    top: 172px;
    width: 280px;
    height: 514px;
    background: linear-gradient(160deg, var(--brand-orange) 0%, var(--brand-orange-soft) 100%);
  }
  .brand {
    position: absolute;
    left: 166px;
    top: 388px;
    width: 706px;
    text-align: center;
    font-family: "Montserrat", Arial, sans-serif;
    font-weight: 500;
  }
  .brand__name {
    margin: 0;
    font-size: 92px;
    font-weight: 500;
    line-height: 1;
    letter-spacing: 0.2em;
    margin-right: -0.2em;
    color: var(--name-grey);
  }
  .brand__slogan {
    margin: 28px 0 0;
    font-size: 19px;
    letter-spacing: 0.32em;
    margin-right: -0.32em;
    color: var(--brand-orange);
  }
</style>
</head>
<body>
  <main class="card">
    <svg class="card__waves" viewBox="0 0 700 400" preserveAspectRatio="none" aria-hidden="true">
      <path class="wave--grey" d="M60,0 C200,0 350,42 500,36 C600,32 660,18 700,8 L700,60 L0,60 Z"/>
      <path class="wave--orange" d="M0,40 C150,18 300,38 450,54 C560,66 640,46 700,40 L700,84 C600,92 500,70 400,76 C250,86 80,120 0,176 Z"/>
    </svg>

    <div class="emblem-area" role="img" aria-label="Brand emblem area in orange"></div>

    <div class="brand">
      <h1 class="brand__name">BRAVOAK</h1>
      <p class="brand__slogan">ASPIRE. TRUST. ACHIEVE.</p>
    </div>
  </main>
</body>
</html>
```